Email Signature

We would like to have an email Signature designed.
We have an idea, and a logo that we would like to be make more professional in design and look.

```html
<!DOCTYPE html>
<html lang="en">
<head>
<meta charset="UTF-8">
<title>Email Signature – Tessa Rowan</title>
<link href="https://fonts.googleapis.com/css2?family=Lato:wght@400;700&display=swap" rel="stylesheet">
<style>
  :root {
    --page-bg: #efefef;
    --card-bg: #ffffff;
    --accent-orange: #f05a28;
    --accent-blue: #1d76c2;
    --wave-grey: #a7a7a7;
    --wave-grey-clear: rgba(167, 167, 167, 0);
    --text-dark: #1e1e1e;
  }
  * { margin: 0; padding: 0; box-sizing: border-box; }
  html, body {
    width: 1200px;
    height: 533px;
    overflow: hidden;
    background: var(--page-bg);
    font-family: "Lato", Arial, sans-serif;
  }
  .canvas {
    position: relative;
    width: 1200px;
    height: 533px;
  }
  .signature {
    position: absolute;
    left: 40px;
    top: 182px;
    width: 1120px;
    height: 168px;
    background: var(--card-bg);
    overflow: hidden;
  }

  .accent-band {
    position: absolute;
    left: 0;
    top: 124px;
    width: 300px;
    height: 22px;
    background: linear-gradient(90deg, var(--accent-blue) 0%, var(--accent-orange) 55%, rgba(240, 90, 40, 0) 100%);
  }
  .grey-field {
    position: absolute;
    right: 0;
    top: 0;
    width: 620px;
    height: 100%;
    background: linear-gradient(100deg, var(--wave-grey-clear) 0%, var(--wave-grey) 40%, var(--wave-grey) 100%);
  }

  .contact {
    position: absolute;
    left: 121px;
    top: 30px;
  }
  .contact__name {
    font-size: 27px;
    font-weight: 700;
    color: var(--accent-orange);
    letter-spacing: 0.3px;
    line-height: 1.1;
  }
  .contact__role {
    margin-top: 4px;
    font-size: 14px;
    color: var(--text-dark);
  }
  .contact__phone {
    margin-top: 10px;
    font-size: 15px;
    color: var(--text-dark);
  }
  .contact__label { color: var(--accent-blue); }

  .brand {
    position: absolute;
    right: 32px;
    top: 62px;
    display: flex;
    align-items: center;
    gap: 12px;
  }
  .brand__dot {
    width: 32px;
    height: 32px;
    border-radius: 50%;
    background: var(--accent-orange);
  }
  .brand__name {
    font-size: 36px;
    font-weight: 700;
    color: var(--accent-blue);
    line-height: 1;
  }
</style>
</head>
<body>
  <main class="canvas">
    <section class="signature">
      <div class="grey-field" role="img" aria-label="Decorative grey wave rising toward the right side of the signature"></div>
      <div class="accent-band" role="img" aria-label="Decorative blue and orange swoosh along the lower left"></div>

      <div class="contact">
        <p class="contact__name">TESSA ROWAN</p>
        <p class="contact__role">Client Relations</p>
        <p class="contact__phone"><span class="contact__label">Mob:</span> +61 400 555 182</p>
      </div>

      <div class="brand">
        <span class="brand__dot"></span>
        <span class="brand__name">Northbay Advisory</span>
      </div>
    </section>
  </main>
</body>
</html>
```